Need a Shoe Box for Women's Luxury Shoe Brand

We need a shoe box design for a new company of women's luxury shoes. The box should be beautiful, unique, interesting and appealing to women of all ages (20-60). I would definitely like to see light pink with our brand name 'Morvessa' in metallic (preferably gold), however please submit ALL your ideas as I am open to and would like to see everything. I would like to see the 'e' logo on the interior of the box. I have also uploaded some design inspirations.

Target Market(s)

Women ages 20-60

Industry/Entity Type

Shoe

Requirements
Nice to have
• The brand name 'Morvessa' in gold (metallic)
• Light pink color
Should not have
• Bright/dark pinks

```html
<!DOCTYPE html>
<html lang="en">
<head>
<meta charset="utf-8">
<title>Morvessa Shoe Box Dieline</title>
<link rel="stylesheet" href="https://fonts.googleapis.com/css2?family=Cinzel:wght@500&display=swap">
<style>
  :root {
    --paper: #ffffff;
    --rose: #ec93b3;
    --rose-stripe: #f9d2e0;
    --blush-band: #f8cadb;
    --trim: #231f20;
    --fold-line: #8a8a8a;
    --gold: #a8802a;
  }
  html, body {
    margin: 0;
    padding: 0;
    width: 815px;
    height: 1200px;
    overflow: hidden;
    background: var(--paper);
  }
  .box-dieline {
    display: block;
    width: 815px;
    height: 1200px;
  }
  .panel-base { fill: var(--rose); }
  .panel-edge { fill: none; stroke: var(--fold-line); stroke-width: 0.6; }
  .stripe { fill: var(--rose-stripe); }
  .rim-band { fill: var(--blush-band); }
  .trim-line { fill: var(--trim); }
  .brand-name {
    font-family: "Cinzel", "Times New Roman", serif;
    font-weight: 500;
    font-size: 20px;
    letter-spacing: 6px;
    fill: var(--gold);
  }
</style>
</head>
<body>
<svg class="box-dieline" viewBox="0 0 784 1152" preserveAspectRatio="none" xmlns="http://www.w3.org/2000/svg" aria-label="Morvessa shoe box dieline">
  <defs>
    <pattern id="stripes-vertical" width="25" height="10" patternUnits="userSpaceOnUse" x="190">
      <rect class="stripe" x="0" y="0" width="5" height="10"/>
    </pattern>
    <pattern id="stripes-horizontal" width="10" height="24.5" patternUnits="userSpaceOnUse" y="300">
      <rect class="stripe" x="0" y="0" width="10" height="4"/>
    </pattern>
  </defs>

  <!-- Top side wall -->
  <g class="wall wall-top">
    <rect class="rim-band" x="181" y="18" width="427" height="54" role="img" aria-label="Soft pink patterned rim band"/>
    <rect class="trim-line" x="181" y="72" width="427" height="5"/>
    <rect class="panel-base" x="181" y="77" width="427" height="213"/>
    <rect fill="url(#stripes-vertical)" x="181" y="77" width="427" height="213"/>
    <rect class="panel-edge" x="181" y="18" width="427" height="272"/>
  </g>

  <!-- Left end wall -->
  <g class="wall wall-left">
    <rect class="rim-band" x="27" y="290" width="53" height="270" role="img" aria-label="Soft pink patterned rim band"/>
    <rect class="trim-line" x="80" y="290" width="5" height="270"/>
    <rect class="panel-base" x="85" y="290" width="96" height="270"/>
    <rect fill="url(#stripes-horizontal)" x="85" y="290" width="96" height="270"/>
    <rect class="panel-edge" x="27" y="290" width="154" height="270"/>
  </g>

  <!-- Box floor -->
  <g class="box-floor">
    <rect class="panel-base" x="181" y="290" width="427" height="270"/>
    <rect class="panel-edge" x="181" y="290" width="427" height="270"/>
  </g>

  <!-- Right end wall -->
  <g class="wall wall-right">
    <rect class="panel-base" x="608" y="290" width="96" height="270"/>
    <rect fill="url(#stripes-horizontal)" x="608" y="290" width="96" height="270"/>
    <rect class="trim-line" x="704" y="290" width="5" height="270"/>
    <rect class="rim-band" x="709" y="290" width="53" height="270" role="img" aria-label="Soft pink patterned rim band"/>
    <rect class="panel-edge" x="608" y="290" width="154" height="270"/>
  </g>

  <!-- Bottom side wall -->
  <g class="wall wall-bottom">
    <rect class="panel-base" x="181" y="560" width="427" height="213"/>
    <rect fill="url(#stripes-vertical)" x="181" y="560" width="427" height="213"/>
    <rect class="trim-line" x="181" y="773" width="427" height="5"/>
    <rect class="rim-band" x="181" y="778" width="427" height="53" role="img" aria-label="Soft pink patterned rim band"/>
    <rect class="panel-edge" x="181" y="560" width="427" height="271"/>
  </g>

  <!-- Lid -->
  <g class="box-lid">
    <rect class="panel-base" x="181" y="840" width="427" height="270"/>
    <rect fill="url(#stripes-vertical)" x="181" y="840" width="427" height="270"/>
    <rect class="panel-edge" x="181" y="840" width="427" height="270"/>
    <text class="brand-name" x="407" y="982" text-anchor="middle">MORVESSA</text>
  </g>
</svg>
</body>
</html>
```